Eastfield Commercial Card

I would like a modern, eye catching card based off my logo design.
Info to include:
Anders Voll (Card Name)
eastfieldcommercial.example (Website)
555 203 8841 (Office/fax)
555 287 3096 (Business Cell)
anders@eastfieldcommercial.example (Work email)

Target Market(s)

Commercial real estate brokers, property owners.

Colors
ec1f27
757575

Requirements
Must have
• Name and info above. Not be lame!:)

```html
<!DOCTYPE html>
<html lang="en">
<head>
<meta charset="utf-8">
<title>Eastfield Commercial – Business Card</title>
<link href="https://fonts.googleapis.com/css2?family=Montserrat:wght@400;500;700;800&display=swap" rel="stylesheet">
<style>
  :root {
    --brand-red: #a51e25;
    --brand-grey: #757575;
    --ink: #2b2b2b;
    --paper: #ffffff;
    --backdrop: #1e1e1e;
    --band-shadow: #4a4a4a;
  }
  * { box-sizing: border-box; margin: 0; padding: 0; }
  html, body {
    width: 1200px; height: 900px; overflow: hidden;
    background: var(--backdrop);
    font-family: "Montserrat", sans-serif;
  }
  .sheet {
    position: relative; width: 1200px; height: 900px;
    display: flex; flex-direction: column; align-items: center; justify-content: center; gap: 48px;
  }
  .card {
    position: relative; width: 630px; height: 360px; border-radius: 18px; overflow: hidden;
  }

  /* Front */
  .card--front {
    background: var(--brand-red);
    color: var(--paper);
    display: flex; flex-direction: column; align-items: center; justify-content: center;
  }
  .front__mark {
    width: 54px; height: 54px; border: 6px solid var(--paper); border-radius: 4px; margin-bottom: 22px;
  }
  .front__name {
    font-weight: 800; font-size: 34px; letter-spacing: 1px; text-transform: uppercase; white-space: nowrap;
  }
  .tagline {
    display: flex; align-items: center; gap: 14px; white-space: nowrap;
    font-weight: 500; font-size: 13px; letter-spacing: 5px; text-transform: uppercase; margin-top: 6px;
  }
  .tagline::before, .tagline::after {
    content: ""; width: 48px; height: 2px; background: currentColor;
  }
  .front__web {
    margin-top: 40px; font-weight: 700; font-size: 14px; white-space: nowrap;
  }

  /* Back */
  .card--back { background: var(--paper); color: var(--ink); }
  .back__brand {
    position: absolute; left: 46px; top: 58px; display: flex; align-items: center; gap: 14px;
  }
  .back__mark {
    width: 40px; height: 40px; border: 5px solid var(--brand-grey); border-radius: 3px; flex: none;
  }
  .back__name {
    font-weight: 800; font-size: 34px; letter-spacing: 1px; text-transform: uppercase; color: var(--brand-red);
    line-height: 1; white-space: nowrap;
  }
  .back__brand .tagline { color: var(--ink); font-size: 13px; margin-top: 6px; }
  .back__details {
    position: absolute; left: 92px; right: 36px; top: 166px;
    display: flex; align-items: center; gap: 24px;
  }
  .person { text-align: right; white-space: nowrap; flex: none; }
  .person__name {
    font-weight: 700; font-size: 16px; color: var(--brand-red); text-transform: uppercase;
  }
  .person__role { font-size: 13px; margin-top: 4px; }
  .divider { width: 2px; height: 74px; background: var(--brand-red); flex: none; }
  .contacts { list-style: none; font-size: 12.5px; line-height: 1.8; white-space: nowrap; }
  .contacts li { display: flex; align-items: center; gap: 12px; }
  .contacts svg { width: 14px; height: 14px; fill: var(--brand-red); flex: none; }
  .back__band {
    position: absolute; left: 0; right: 0; bottom: 0; height: 28px;
    background: var(--brand-red);
    border-top: 5px solid var(--band-shadow);
  }
</style>
</head>
<body>
<main class="sheet">
  <section class="card card--front" aria-label="Card front">
    <div class="front__mark"></div>
    <h1 class="front__name">Eastfield Commercial</h1>
    <p class="tagline">Construction &amp; Roofing</p>
    <p class="front__web">www.eastfieldcommercial.example</p>
  </section>

  <section class="card card--back" aria-label="Card back">
    <div class="back__brand">
      <div class="back__mark"></div>
      <div>
        <h2 class="back__name">Eastfield Commercial</h2>
        <p class="tagline">Construction &amp; Roofing</p>
      </div>
    </div>
    <div class="back__details">
      <div class="person">
        <p class="person__name">Anders Voll</p>
        <p class="person__role">Director / Founder</p>
      </div>
      <div class="divider"></div>
      <ul class="contacts">
        <li><svg viewBox="0 0 24 24"><path d="M6.6 10.8a15 15 0 0 0 6.6 6.6l2.2-2.2a1 1 0 0 1 1-.25 11.4 11.4 0 0 0 3.6.57 1 1 0 0 1 1 1V20a1 1 0 0 1-1 1A17 17 0 0 1 3 4a1 1 0 0 1 1-1h3.5a1 1 0 0 1 1 1c0 1.25.2 2.45.57 3.57a1 1 0 0 1-.25 1z"/></svg>555 203 8841</li>
        <li><svg viewBox="0 0 24 24"><path d="M6 2h9v6H6zM3 9h18a1 1 0 0 1 1 1v8h-4v4H6v-4H2v-8a1 1 0 0 1 1-1zm5 7v4h8v-4z"/></svg>555 287 3096</li>
        <li><svg viewBox="0 0 24 24"><path d="M2 5h20v14H2zm2 2v.5l8 5 8-5V7l-8 5z"/></svg>anders@eastfieldcommercial.example</li>
      </ul>
    </div>
    <div class="back__band"></div>
  </section>
</main>
</body>
</html>
```